Redesign wellness clinic website

The project is redesign a wellness clinic http://www.thornleighvitality.example. The new website is to be responsive,clean,bright and a strong call to action which is to book an appointment. The logo will remain the same but the colour scheme on the website should be reflect purple white and green. I want it to be bright and cheerful and the feeling of clarity. The website shouldn't be overloaded with content but more visuals.

Target Market(s)

Anyone that has corporate wellness benefits within the downtown Toronto core. Majority of audience are professional working in Media, Telecommunications and Investments.

Industry/Entity Type

Health And Wellness

Number of Pages Required

5+ page

Font styles to use
Sans Serif

Colors
ffffff
886aae
acd036

Requirements
Must have
• -Strong call to action which is book an appointment like this page https://www.kestrelmotion.example/
• -Services provided icons on the page like https://www.brightpathvitalityhouse.example/
• - Pictures of a good visualizing a fit and healthy life
• - Strong ratings from Quorva, Zintrel, PostMaz, similar to this website http://www.summitbalancehealth.example/our-team-professionals/
• - Bright and clear
Should not have
• -No black and white images (redo our pictures)
• -Dark themes

```html
<!DOCTYPE html>
<html lang="en">
<head>
<meta charset="utf-8">
<title>Thornleigh Vitality Centre</title>
<link href="https://fonts.googleapis.com/css2?family=Open+Sans:wght@400;600;700;800&display=swap" rel="stylesheet">
<style>
:root{
  --purple:#886aae;
  --purple-dark:#6e5296;
  --purple-light:#a995c6;
  --purple-soft:#f1ecf7;
  --green:#acd036;
  --green-dark:#95bb26;
  --green-soft:#f0f6dd;
  --white:#ffffff;
  --ink:#4a4a4a;
  --muted:#8a8a8a;
  --line:#e3e3e3;
}
*{box-sizing:border-box;margin:0;padding:0}
html,body{width:1200px;height:5357px;overflow:hidden}
body{font-family:"Open Sans",Arial,sans-serif;color:var(--ink);background:var(--white);font-size:13px;line-height:1.6;position:relative}
h2.section-title{font-size:34px;font-weight:800;text-align:center;color:var(--purple);letter-spacing:1px;text-transform:uppercase}
h2.section-title span{color:var(--ink)}
.intro{text-align:center;color:var(--muted);font-size:13px;max-width:900px;margin:12px auto 0}
.btn-outline{display:inline-block;border:1px solid var(--purple);color:var(--purple);padding:6px 26px;border-radius:16px;font-size:11px;font-weight:700;text-transform:uppercase}
.arrow{position:absolute;width:30px;height:30px;border-radius:50%;background:#d8d8d8;display:flex;align-items:center;justify-content:center}

/* header */
.topbar{height:40px;display:flex;justify-content:space-between;align-items:center;font-size:11px;color:var(--muted);padding:0 70px;border-bottom:1px solid var(--line)}
.masthead{height:74px;display:flex;align-items:center;justify-content:space-between;padding:0 70px}
.brand{display:flex;align-items:center;gap:10px;font-weight:700;color:var(--purple);font-size:16px}
.brand i{width:40px;height:40px;border-radius:50%;background:var(--green);display:block}
.head-actions{display:flex;gap:14px}
.phone-pill{border:2px solid var(--green);color:var(--green-dark);border-radius:22px;padding:8px 22px;font-weight:700;font-size:15px;display:flex;align-items:center;gap:8px}
.cta{background:var(--green);color:#fff;border-radius:22px;padding:10px 26px;font-weight:700;font-size:14px;text-transform:uppercase}
.nav{height:44px;display:flex;padding:0 70px;border-top:1px solid var(--line);border-bottom:1px solid var(--line)}
.nav a{padding:0 20px;line-height:42px;font-size:12px;font-weight:600;color:var(--ink);text-transform:uppercase;text-decoration:none}
.nav a.active{color:var(--purple);border-bottom:3px solid var(--purple)}

/* hero */
.hero{height:413px;position:relative;background:linear-gradient(90deg,#f4f6f8 0%,#e6ecef 40%,#d5e3ea 70%,#f0d9c8 100%)}
.hero-copy{position:absolute;left:70px;top:70px}
.hero-copy h1{font-size:54px;line-height:1.05;font-weight:800;color:var(--purple);text-transform:uppercase}
.hero-copy p{margin-top:10px;font-size:22px;font-weight:800;color:var(--green-dark);text-transform:uppercase}

/* services */
.services{display:flex;height:244px}
.service{flex:1;color:#fff;text-align:center;padding:26px 36px 0}
.service .ico{width:80px;height:80px;border-radius:50%;border:2px solid rgba(255,255,255,.8);margin:0 auto 14px;display:flex;align-items:center;justify-content:center}
.service h3{font-size:16px;font-weight:800;text-transform:uppercase}
.service p{font-size:12px;line-height:1.5;margin-top:4px}
.s1{background:#b8d64d}.s2{background:var(--green-dark)}.s3{background:var(--purple)}.s4{background:var(--purple-light)}

/* about */
.about{height:505px;position:relative}
.about .text{position:absolute;left:70px;top:70px;width:560px}
.about h2{font-size:32px;font-weight:800;color:var(--purple);text-transform:uppercase}
.about h2 span{color:var(--ink)}
.about p{margin-top:16px;font-size:13px;color:var(--ink)}
.about p a{color:var(--purple);font-weight:600}
.about .photo{position:absolute;right:0;top:60px;width:520px;height:420px;background:radial-gradient(ellipse at 60% 50%,#eef2f5 0%,#dfe6ec 60%,#fff 100%)}

/* ratings */
.ratings{height:237px;background:var(--green-soft);position:relative;padding-top:22px}
.ratings h4{text-align:center;font-size:12px;font-weight:700;color:var(--purple);text-transform:uppercase}
.badges{display:flex;justify-content:center;gap:40px;margin-top:30px}
.badge{width:200px;height:120px;background:#fff;border:1px solid var(--line);display:flex;align-items:center;justify-content:center}

/* staff */
.staff{height:714px;position:relative;padding-top:55px}
.team{display:flex;justify-content:center;gap:42px;margin-top:40px}
.member{width:300px;text-align:center}
.member .pic{height:320px;background:linear-gradient(160deg,#f0eef2,#d9d6de)}
.member h5{margin-top:12px;color:var(--purple);font-size:13px;font-weight:700}
.member small{display:block;color:var(--muted);font-size:11px}

/* booking */
.booking{height:572px;position:relative;background:#f7f7f9}
.booking .photo{position:absolute;left:0;top:0;width:560px;height:572px;background:linear-gradient(135deg,#eef3f8 0%,#cfe0ee 55%,#7fa4c8 100%)}
.booking .form{position:absolute;left:600px;top:50px;width:530px}
.booking h2{font-size:32px;font-weight:800;color:var(--purple);text-transform:uppercase}
.field-row{display:flex;gap:20px;margin-top:16px}
.field{flex:1;height:40px;border:1px solid var(--line);background:#fff;font-size:12px;color:var(--muted);padding:10px 14px}
.field.area{height:130px}
.submit{margin-top:18px;display:inline-block;background:var(--green);color:#fff;font-weight:700;padding:9px 34px;border-radius:20px;font-size:13px}

/* testimonials */
.testimonials{height:625px;position:relative;padding-top:55px;background:linear-gradient(#fff,#f6f3fa)}
.quotes{display:flex;gap:40px;justify-content:center;margin-top:40px}
.quote{width:490px;background:#fff;border:1px solid var(--line);padding:28px 34px;font-style:italic;font-size:12px;color:var(--ink);position:relative}
.quote cite{display:block;margin-top:14px;font-style:normal;font-weight:700;font-size:11px;color:var(--purple);text-transform:uppercase}
.quote cite small{display:block;font-weight:400;color:var(--muted);text-transform:none}

/* news */
.news{height:732px;padding-top:55px;position:relative}
.cards{display:flex;gap:40px;justify-content:center;margin-top:40px}
.card{width:326px}
.card .pic{height:270px;position:relative}
.card .date{position:absolute;right:0;bottom:0;background:var(--green);color:#fff;font-size:11px;font-weight:700;padding:6px 14px}
.card h5{margin-top:16px;font-size:16px;font-weight:700;color:var(--ink)}
.card p{margin:8px 0 16px;font-size:12px;color:var(--muted)}

/* tips faq */
.tips{height:732px;position:relative;padding-top:20px}
.tips .col-l{position:absolute;left:70px;top:30px;width:540px}
.tips .col-r{position:absolute;left:660px;top:30px;width:470px}
.tips h3{font-size:30px;font-weight:800;color:var(--purple);text-transform:uppercase}
.tips h3 span{color:var(--ink)}
.tabs{display:flex;margin-top:20px;border-bottom:2px solid var(--purple)}
.tabs span{padding:8px 20px;font-size:12px;color:var(--purple);font-weight:600}
.tabs span.on{background:var(--purple);color:#fff}
.tip-body{display:flex;gap:26px;margin-top:20px}
.tip-body p{font-size:12px;font-style:italic;color:var(--muted);flex:1}
.doc{width:150px;text-align:center}
.doc i{display:block;width:130px;height:130px;border-radius:50%;background:linear-gradient(#e7e4ec,#c9c3d3);margin:0 auto 8px}
.doc b{display:block;font-size:11px;color:var(--purple)}
.doc small{font-size:10px;color:var(--muted)}
.faq-item{margin-top:14px;display:flex;align-items:center;gap:12px;font-size:14px;font-weight:600;color:var(--ink)}
.faq-item i{width:28px;height:28px;background:var(--purple);color:#fff;font-style:normal;display:flex;align-items:center;justify-content:center;font-weight:700}
.faq-open{margin-top:20px;background:var(--purple);color:#fff;padding:9px 14px;font-weight:700;font-size:14px;display:flex;gap:12px}
.faq-open + p{border:1px solid var(--line);border-top:0;padding:16px;font-size:12px;color:var(--muted)}

/* footer */
.footer{position:absolute;left:0;top:5017px;width:1200px;height:304px;background:var(--purple);color:#fff}
.footer h6{font-size:15px;font-weight:700;text-transform:uppercase;border-bottom:1px solid rgba(255,255,255,.35);padding-bottom:8px}
.fcol{position:absolute;top:38px}
.fcol p{font-size:11px;margin-top:10px;line-height:1.5}
.hours{width:100%;font-size:11px;margin-top:8px;border-collapse:collapse}
.hours td{padding:3px 0}
.hours td:last-child{text-align:right}
.map{position:absolute;right:0;top:0;width:300px;height:304px;background:linear-gradient(135deg,#eceff0 0%,#dde5d8 100%)}
.copyright{position:absolute;left:0;top:5321px;width:1200px;height:36px;background:var(--purple-dark);color:#fff;font-size:11px;line-height:36px;padding-left:70px}
</style>
</head>
<body>

<header>
  <div class="topbar">
    <span>Hours: Monday – Friday 7:30am – 9pm, Saturday 10am – 5pm, Sunday 10am – 4pm</span>
    <span>hello@thornleighvitality.example</span>
  </div>
  <div class="masthead">
    <div class="brand"><i></i>Thornleigh Vitality Centre</div>
    <div class="head-actions">
      <span class="phone-pill"><svg width="16" height="16" viewBox="0 0 24 24"><path d="M6.6 10.8a15 15 0 0 0 6.6 6.6l2.2-2.2a1 1 0 0 1 1-.25 11.4 11.4 0 0 0 3.6.6 1 1 0 0 1 1 1V20a1 1 0 0 1-1 1A17 17 0 0 1 3 4a1 1 0 0 1 1-1h3.5a1 1 0 0 1 1 1 11.4 11.4 0 0 0 .6 3.6 1 1 0 0 1-.25 1z" fill="#95bb26"/></svg>416-555-0142</span>
      <span class="cta">Make an appointment</span>
    </div>
  </div>
  <nav class="nav">
    <a class="active">Home</a><a>Fees &amp; Services</a><a>Our Staff</a><a>News &amp; Updates</a><a>Corporate Wellness</a><a>Forms</a><a>Contact Us</a>
  </nav>
</header>

<section class="hero" role="img" aria-label="Smiling patient with a clinician in a bright treatment room">
  <div class="hero-copy">
    <h1>Fit for life<br>wellness &amp;<br>rehab centre</h1>
    <p>Chiropractic • Physiotherapy • Massage</p>
  </div>
</section>

<section class="services">
  <div class="service s1">
    <div class="ico"><svg width="40" height="40" viewBox="0 0 40 40"><circle cx="20" cy="20" r="6" fill="none" stroke="#fff" stroke-width="2"/><path d="M20 4v8M20 28v8M4 20h8M28 20h8" stroke="#fff" stroke-width="2"/></svg></div>
    <h3>Chiropractic</h3><p>Chiropractic care can help you with neck, back and other joint related injuries.</p>
  </div>
  <div class="service s2">
    <div class="ico"><svg width="40" height="40" viewBox="0 0 40 40"><rect x="8" y="8" width="24" height="24" rx="4" fill="none" stroke="#fff" stroke-width="2"/><path d="M20 13v14M13 20h14" stroke="#fff" stroke-width="2"/></svg></div>
    <h3>Physiotherapy</h3><p>Physiotherapy can help you recover from a car accident to sports related injury.</p>
  </div>
  <div class="service s3">
    <div class="ico"><svg width="40" height="40" viewBox="0 0 40 40"><path d="M20 32s-11-7-11-15a6 6 0 0 1 11-3 6 6 0 0 1 11 3c0 8-11 15-11 15z" fill="none" stroke="#fff" stroke-width="2"/></svg></div>
    <h3>Massage Therapy</h3><p>Massage therapy is one of the oldest forms of natural therapy.</p>
  </div>
  <div class="service s4">
    <div class="ico"><svg width="40" height="40" viewBox="0 0 40 40"><path d="M12 21l6 6 11-13" fill="none" stroke="#fff" stroke-width="2.5"/></svg></div>
    <h3>Nutritionist</h3><p>Wholesome nutrition choices can help you reach your healthiest goals.</p>
  </div>
</section>

<section class="about">
  <div class="text">
    <h2>About <span>Thornleigh Vitality</span></h2>
    <p>Established in 1993 the Thornleigh Vitality Centre has become one of the city's leaders in providing quality care and innovative wellness programs for the community. The founder and director has grown the clinic from a small practice to a team of over 30 practitioners providing a multitude of different services under one roof. Some of the services include Chiropractic, Physiotherapy, Athletic Therapy, Naturopathy, Massage Therapy, Acupuncture and Personal Training. The centre also has a complete fitness studio on its premises. We also offer many wellness seminars free of cost to the public.</p>
    <p>Our Centre is committed to helping improve and extend the lives of as many people as possible in our community. Come and join our family and start changing your life today. <a>Read more »</a></p>
  </div>
  <div class="photo" role="img" aria-label="Group of smiling clinicians in white coats"></div>
</section>

<section class="ratings">
  <h4>Thornleigh Vitality Centre Rating &amp; Facts</h4>
  <div class="badges">
    <div class="badge" aria-label="Physician badge"><svg width="150" height="80"><rect x="0" y="0" width="150" height="80" rx="6" fill="#f1ecf7"/></svg></div>
    <div class="badge" aria-label="Zintrel reviews badge"><svg width="150" height="80"><rect x="0" y="0" width="150" height="80" rx="6" fill="#e9eef6"/></svg></div>
    <div class="badge" aria-label="Quorva rating badge"><svg width="150" height="80"><rect x="0" y="0" width="150" height="80" rx="6" fill="#f3dcdc"/></svg></div>
    <div class="badge" aria-label="PostMaz award badge"><svg width="150" height="80"><circle cx="75" cy="40" r="36" fill="#e3efc6"/></svg></div>
  </div>
  <span class="arrow" style="left:70px;top:110px"><svg width="10" height="12"><path d="M8 1L2 6l6 5" fill="none" stroke="#fff" stroke-width="2"/></svg></span>
  <span class="arrow" style="right:70px;top:110px"><svg width="10" height="12"><path d="M2 1l6 5-6 5" fill="none" stroke="#fff" stroke-width="2"/></svg></span>
</section>

<section class="staff">
  <h2 class="section-title">Meet <span>our staff</span></h2>
  <p class="intro">Thornleigh Vitality has Chiropractic, Physiotherapy, Active Rehabilitation, Massage Therapy, Nutrition and Lifestyle Medicine, Chiropody, Osteopathy &amp; Administration Staff for your help 24/7.</p>
  <div class="team">
    <div class="member"><div class="pic" role="img" aria-label="Portrait of the clinic director"></div><h5>Dr. Alden Voss</h5><small>Chiropractor, Director of Clinic</small></div>
    <div class="member"><div class="pic" role="img" aria-label="Portrait of the head physiotherapist"></div><h5>Mira Lenko</h5><small>Head of Rehabilitation Department, Registered Physiotherapist</small></div>
    <div class="member"><div class="pic" role="img" aria-label="Portrait of the fascial stretch therapist"></div><h5>Tobias Renn</h5><small>Fascial Stretch Therapist, Kinesiologist</small></div>
  </div>
  <span class="arrow" style="left:70px;top:310px"><svg width="10" height="12"><path d="M8 1L2 6l6 5" fill="none" stroke="#fff" stroke-width="2"/></svg></span>
  <span class="arrow" style="right:70px;top:310px"><svg width="10" height="12"><path d="M2 1l6 5-6 5" fill="none" stroke="#fff" stroke-width="2"/></svg></span>
</section>

<section class="booking">
  <div class="photo" role="img" aria-label="Clinician in a white coat writing on a blue clipboard"></div>
  <div class="form">
    <h2>Book appointment</h2>
    <div class="field-row"><div class="field">Name</div></div>
    <div class="field-row"><div class="field">Phone</div><div class="field">E-mail</div></div>
    <div class="field-row"><div class="field">Date</div><div class="field">Time</div></div>
    <div class="field-row"><div class="field area">Your Message...</div></div>
    <span class="submit">SUBMIT</span>
  </div>
</section>

<section class="testimonials">
  <h2 class="section-title">Testimonials</h2>
  <p class="intro">As part of our commitment to serve our community we provide corporate wellness programs &amp; corporate wellness fairs for neighbouring corporations. Our wellness fairs include onsite chair massage from a Registered Massage Therapist, posture checks, presentations and much more. For more details please feel free to email Omar Brenn via email at hello@thornleighvitality.example</p>
  <div class="quotes">
    <div class="quote">On behalf of the staff at the Aldermoor Fertility Centre, we would like to thank the professionals at Thornleigh Vitality for participating in our staff appreciation day. The complimentary mini-massages and posture checks were a great addition to the event. Your staff, made our staff feel taken care of and appreciated. We are happy to encourage our staff to use your full range of health services and know that they will be well looked after.
      <cite>Marisa Cole,<small>Aldermoor Fertility Centre</small></cite></div>
    <div class="quote">As part of our Brightfield Fund fundraiser, we reached out to Thornleigh Vitality Centre to see if they would lend a helping hand in our Wellness Charity Day to lay dedicated to raising funds and promoting a healthy lifestyle. I spoke with Omar Brenn and he immediately offered to help us with our event by donating gift packages for us to raffle off and a friendly team to provide 15-minute massages and posture checks during our event. The Thornleigh Vitality Centre team was very professional, well organized and enthusiastic. We thank them for a successful charity event.
      <cite>Priya Danek,<small>Event Lead</small></cite></div>
  </div>
  <span class="arrow" style="left:70px;top:330px"><svg width="10" height="12"><path d="M8 1L2 6l6 5" fill="none" stroke="#fff" stroke-width="2"/></svg></span>
  <span class="arrow" style="right:70px;top:330px"><svg width="10" height="12"><path d="M2 1l6 5-6 5" fill="none" stroke="#fff" stroke-width="2"/></svg></span>
</section>

<section class="news">
  <h2 class="section-title">News <span>&amp; Updates</span></h2>
  <p class="intro">We will always keep you informed about fresh news at our clinic. Moreover, you will find useful articles about care, the newest technologies in treatment, and interesting events related to wellness and medicine in general.</p>
  <div class="cards">
    <div class="card"><div class="pic" role="img" aria-label="Athlete body showing muscles in motion" style="background:linear-gradient(135deg,#2d3f6b,#d8893a)"><span class="date">01.05.2016</span></div>
      <h5>Think Well Program</h5><p>Did you know that your mental wellness can directly affect your physical wellness and vice versa? Our Think Well program pairs counselling with body care.</p><span class="btn-outline">Read more</span></div>
    <div class="card"><div class="pic" role="img" aria-label="Therapist treating a patient's lower leg" style="background:linear-gradient(135deg,#f2eeee,#c9b7b0)"><span class="date">01.05.2016</span></div>
      <h5>Feel Fascia Facts</h5><p>Did you know that our muscles, bones and organs are covered by a net-like web of fascia? Releasing it can ease tension and help you move freely.</p><span class="btn-outline">Read more</span></div>
    <div class="card"><div class="pic" role="img" aria-label="Notice with summer office hours" style="background:linear-gradient(135deg,#e8f0f5,#c7dbe8)"><span class="date">01.05.2016</span></div>
      <h5>6 Ways Physiotherapy can help relieve Aches and Pains</h5><p>Physiotherapy is a healthcare service that enhances the quality of life of people through exercise and hands-on care.</p><span class="btn-outline">Read more</span></div>
  </div>
</section>

<section class="tips">
  <div class="col-l">
    <h3>Top tips <span>from doctors</span></h3>
    <div class="tabs"><span class="on">Massage Therapy</span><span>Osteopathy</span><span>Active Rehabilitation</span></div>
    <div class="tip-body">
      <p>Tooth whitening (termed tooth bleaching when utilizing bleach) is either restoration of natural tooth shade or whitening beyond natural tooth shade, depending on the definition used.<br><br>Restoration of the underlying natural tooth shade is possible by simple removing surface extrinsic stains and calculus. Regular care keeps results lasting longer.</p>
      <div class="doc"><i role="img" aria-label="Portrait of the registered massage therapist"></i><b>Lena Orlov</b><small>Reflexologist, Registered Massage Therapist</small></div>
    </div>
    <span class="btn-outline" style="margin-top:20px">Read more</span>
  </div>
  <div class="col-r">
    <h3>FAQ</h3>
    <div class="faq-open"><span>−</span>Chiropractic Consultation</div>
    <p>Dental implant placement is no longer performed only by oral surgeons and periodontists; general dentists are also increasingly providing difficult surgical implant services. Dental implants may be used to replace single teeth, replace multiple teeth, or provide abutments for complete dentures or partials.</p>
    <div class="faq-item"><i>+</i>Physiotherapy / Athletic Therapy</div>
    <div class="faq-item"><i>+</i>Private Personal Training / Private Pilates</div>
    <div class="faq-item"><i>+</i>Massage Therapy</div>
    <div class="faq-item"><i>+</i>Naturopathy</div>
  </div>
</section>

<footer class="footer">
  <div class="fcol" style="left:70px;width:230px">
    <h6>Latest Tweets</h6>
    <p>@thornleigh<br>Weekly stretch tips for desk workers are now on our blog.<br>2 hours ago</p>
    <p>@thornleigh<br>Book your spring posture check today at the front desk.<br>1 day ago</p>
  </div>
  <div class="fcol" style="left:340px;width:240px">
    <h6>Opening Hours</h6>
    <table class="hours">
      <tr><td>Monday</td><td>07:30 am – 09:00 pm</td></tr>
      <tr><td>Tuesday</td><td>07:30 am – 09:00 pm</td></tr>
      <tr><td>Wednesday</td><td>07:30 am – 09:00 pm</td></tr>
      <tr><td>Thursday</td><td>07:30 am – 09:00 pm</td></tr>
      <tr><td>Friday</td><td>07:30 am – 09:00 pm</td></tr>
      <tr><td>Saturday</td><td>10:00 am – 05:00 pm</td></tr>
      <tr><td>Sunday</td><td>10:00 am – 04:00 pm</td></tr>
    </table>
  </div>
  <div class="fcol" style="left:620px;width:230px">
    <h6>Contacts</h6>
    <p>416-555-0142</p>
    <p>88 Harlow Street, Suite 200<br>Toronto, Ontario</p>
    <p>hello@thornleighvitality.example</p>
  </div>
  <div class="map" role="img" aria-label="Street map showing the clinic location"></div>
</footer>
<div class="copyright">Copyright © 2017 Thornleigh Vitality Centre.</div>

</body>
</html>
```